Venture Capital Investment Firm

We are looking to overhaul our existing website (substantially), with only using the same logos (which we can provide).
We are an investment firm that focuses on making loans to late stage technology companies. Our site should ultimately look like other venture capital firms, and look modern and fresh. We have an existing website www.northvaleloan.com which this will be replacing, although we will be using a lot of the existing written content, and potentially the numbers of pages we will need, we are not wed to anything else. Please feel free to shoot any questions at any time and thank you in advance for your help!
Websites we like as examples:
https://www.tkbrandel.com/
https://www.emberwoodfunds.com/
Target Market(s)
Potential investors who will invest in our firm, as well as potentially companies that are looking to borrow money from us.

```html
<!DOCTYPE html>
<html lang="en">
<head>
<meta charset="utf-8">
<title>Northvale Loan Investment Partners</title>
<link href="https://fonts.googleapis.com/css2?family=Montserrat:wght@700;800&family=Nunito+Sans:wght@300;400;600;700&family=Nunito:wght@500;600;700&display=swap" rel="stylesheet">
<style>
:root{
  --navy:#07073f;
  --navy-deep:#06063a;
  --heading:#1f3c6e;
  --text:#8a8f99;
  --dark-text:#1d1d2b;
  --tint:#eef6fc;
  --line:#cfe6f4;
  --band-a:#2c66b0;
  --band-b:#3fa3e0;
  --white:#ffffff;
  --light-bg:#f6f8fb;
}
*{box-sizing:border-box;margin:0;padding:0}
html,body{width:1200px;height:3707px;overflow:hidden}
body{position:relative;background:var(--white);font-family:"Nunito Sans",sans-serif;color:var(--text)}
.abs{position:absolute}
a{color:inherit;text-decoration:none}

/* header */
.brand{left:80px;top:24px;display:flex;align-items:center;gap:12px}
.brand-mark{width:40px;height:40px;border-radius:50%;background:var(--navy)}
.brand-name{font-family:"Nunito",sans-serif;font-weight:600;color:var(--navy);font-size:30px;letter-spacing:1px;line-height:1}
.brand-sub{font-family:"Nunito",sans-serif;font-weight:600;color:var(--navy);font-size:9px;letter-spacing:.5px;margin-top:3px}
.contact-item{display:flex;gap:14px;font-size:13px;line-height:14px;color:#555}
.contact-item b{color:var(--dark-text);font-weight:700;display:block}
.nav{left:80px;top:100px;display:flex;font-size:11px;font-weight:600;color:#222;letter-spacing:.3px}
.nav a{padding:20px 18px 0;height:50px}
.nav a.active{border-top:3px solid var(--navy);padding-left:18px;padding-right:18px}

/* hero */
.hero{left:0;top:151px;width:1200px;height:563px;background:linear-gradient(100deg,#3a3d44 0%,#7c7f86 40%,#c9cbcd 70%,#e3e1dc 100%)}
.hero-kicker{left:80px;top:326px;color:#fff;font-family:"Montserrat",sans-serif;font-weight:700;font-size:13px;letter-spacing:2px}
.hero-title{left:80px;top:346px;color:#fff;font-family:"Montserrat",sans-serif;font-weight:800;font-size:38px;line-height:45px}
.btn{display:inline-flex;align-items:center;justify-content:center;background:var(--navy);color:#fff;border-radius:30px;font-size:14px;font-weight:600}
.hero-dots{left:588px;top:640px;display:flex;gap:10px}
.hero-dots span{width:8px;height:8px;border-radius:50%;background:#fff}
.hero-dots span.on{background:var(--navy)}

/* services */
.story{left:80px;top:744px;width:408px;height:694px;border:4px solid var(--line);padding:20px 19px}
.photo{background:linear-gradient(135deg,#cfd9e4,#8b96a6 50%,#dfe4ea)}
.story h3{font-family:"Nunito",sans-serif;font-weight:700;color:var(--heading);font-size:19px;margin:22px 0 12px}
.story p{font-size:13.5px;line-height:27px;margin-bottom:14px}
.sec-title{font-family:"Nunito",sans-serif;font-weight:600;color:var(--heading)}
.svc{width:284px;height:237px;background:var(--tint);text-align:center;padding-top:30px;clip-path:polygon(0 0,236px 0,100% 48px,100% 100%,0 100%)}
.svc h4{font-family:"Nunito",sans-serif;font-weight:600;color:var(--heading);font-size:18px;margin:14px 0 10px}
.svc p{font-size:13.5px;line-height:27px;padding:0 28px}
.svc.dark{background:var(--navy)}
.svc.dark h4,.svc.dark p{color:#fff}

/* band */
.band{left:0;width:1200px;background:linear-gradient(90deg,var(--band-a),var(--band-b))}
.stats{left:80px;top:1624px;width:1040px;height:144px;background:#fff;box-shadow:0 6px 20px rgba(0,0,0,.07);display:flex;padding:36px 0 0 28px}
.stat{width:253px}
.stat .num{font-family:"Nunito",sans-serif;font-size:38px;color:var(--dark-text);line-height:40px}
.stat .num::after{content:"";display:block;width:32px;height:2px;background:var(--navy);margin-top:8px}
.stat .lbl{font-size:13px;font-weight:700;letter-spacing:1.5px;color:var(--dark-text);margin-top:12px}

/* blog */
.post{width:327px;border:4px solid var(--line);background:#fff}
.post .img{height:255px;position:relative}
.date{position:absolute;left:0;bottom:0;width:42px;height:95px;background:var(--navy);color:#fff;text-align:center;padding-top:10px;font-size:11px;line-height:21px}
.date b{font-size:19px;display:block;font-weight:700}
.post .body{padding:24px 22px 28px}
.post h5{font-family:"Nunito",sans-serif;font-weight:500;font-size:18px;line-height:28px;color:var(--dark-text);margin-bottom:16px}
.post p{font-size:13.5px;line-height:27px;margin-bottom:22px}
.btn-sm{height:34px;padding:0 12px;font-size:14px}

/* clients */
.clients{left:0;top:2570px;width:1200px;height:610px;background:var(--light-bg)}
.quote{width:327px;height:248px;border:4px solid var(--line);background:#fff;padding:20px 18px 0 20px;display:flex;gap:20px}
.avatar{width:84px;height:84px;border-radius:50%;flex:none;background:linear-gradient(135deg,#c9c9c9,#6f6f70)}
.quote p{font-size:14px;line-height:27px;color:#555}
.quote .name{font-family:"Nunito",sans-serif;font-size:18px;color:var(--dark-text);margin-top:14px}
.quote .role{font-size:12px;color:#555;margin-top:8px}
.qmark{font-family:"Montserrat",sans-serif;font-weight:800;font-size:70px;color:var(--navy);line-height:1}
.c-dots{left:558px;top:3132px;display:flex;gap:10px}
.c-dots span{width:8px;height:8px;border-radius:50%;background:#c8ccd3}
.c-dots span.on{background:var(--navy)}

/* footer */
.footer{left:0;top:3324px;width:1200px;height:383px;background:var(--navy-deep);color:#fff}
.footer h6{font-family:"Nunito",sans-serif;font-weight:700;font-size:18px;color:#fff}
.f-row{display:flex;gap:20px;font-size:12.5px;line-height:17px}
.f-links{font-size:12.5px;line-height:23px;color:#d6d6e6}
.social{display:flex;gap:20px}
.social span{width:34px;height:34px;border-radius:50%;background:#1b1b55}
.sub-input{width:240px;height:48px;background:#1b1b55;display:flex;align-items:center;justify-content:center;font-size:14px;color:#d6d6e6}
.sub-btn{width:240px;height:48px;background:#7a7a7e;display:flex;align-items:center;justify-content:center;font-size:14px}
</style>
</head>
<body>

<!-- header -->
<div class="abs brand">
  <span class="brand-mark"></span>
  <div><div class="brand-name">NORTHVALE LOAN</div><div class="brand-sub">INVESTMENT PARTNERS</div></div>
</div>
<div class="abs contact-item" style="left:600px;top:32px">
  <svg width="20" height="20" viewBox="0 0 20 20"><path d="M19 1 1 9l7 3 3 7z" fill="#222"/></svg>
  <div><b>Email</b>youremail@email.com</div>
</div>
<div class="abs contact-item" style="left:800px;top:32px">
  <svg width="16" height="16" viewBox="0 0 24 24"><path d="M6.6 10.8a15 15 0 0 0 6.6 6.6l2.2-2.2a1 1 0 0 1 1-.2 11 11 0 0 0 3.6.6 1 1 0 0 1 1 1V20a1 1 0 0 1-1 1A17 17 0 0 1 3 4a1 1 0 0 1 1-1h3.5a1 1 0 0 1 1 1c0 1.2.2 2.5.6 3.6a1 1 0 0 1-.2 1z" fill="#222"/></svg>
  <div><b>Call</b>Call Us: +1 555<br>0198 44</div>
</div>
<nav class="abs nav">
  <a class="active">HOME</a><a>STRATEGY</a><a>ABOUT US</a><a>TEAM</a><a>NEWS</a><a>CAREER</a><a>CONTACT</a><a>INVESTORS</a>
</nav>

<!-- hero -->
<div class="abs hero" role="img" aria-label="Photo of smiling business people in a bright office, one holding a tablet"></div>
<div class="abs hero-kicker">WE ARE A GLOBAL STRUCTURED CREDIT INVESTMENT FIRM</div>
<h1 class="abs hero-title">FOCUSED ON THE HEALTHCARE<br>&amp; TECHNOLOGY INDUSTRIES</h1>
<a class="abs btn" style="left:80px;top:475px;width:132px;height:54px">Our Services</a>
<div class="abs hero-dots"><span></span><span class="on"></span></div>

<!-- services -->
<div class="abs story">
  <div class="photo" style="height:282px" role="img" aria-label="Photo of a business team meeting around a table"></div>
  <h3>Read Our Success Story for Inspiration</h3>
  <p>Far far away, behind the word mountains, far from the countries Vokalia and Consonantia, there live the blind texts. Separated they live in Bookmarksgrove right at the coast of the Semantics, a large language ocean.</p>
  <p>On her way she met a copy. The copy warned the Little Blind Text, that where it came from it would have been rewritten a thousand times and everything that was left from its origin would be the word.</p>
  <a class="btn" style="width:118px;height:52px;margin-top:4px">Contact us</a>
</div>
<h2 class="abs sec-title" style="left:525px;top:746px;font-size:30px">Our Best Services</h2>
<p class="abs" style="left:525px;top:812px;width:600px;font-size:13.5px;line-height:27px">On her way she met a copy. The copy warned the Little Blind Text, that where it came from it would have been rewritten a thousand times and everything that was left from its origin would be the word.</p>

<div class="abs svc dark" style="left:525px;top:937px">
  <svg width="50" height="50" viewBox="0 0 50 50" fill="none" stroke="#fff" stroke-width="2"><circle cx="25" cy="12" r="5"/><circle cx="10" cy="36" r="5"/><circle cx="40" cy="36" r="5"/><path d="M18 20a12 12 0 0 0-8 10M32 20a12 12 0 0 1 8 10M17 40h16"/></svg>
  <h4>Organization</h4><p>Far far away, behind the word mountains, far from the countries Vokalia.</p>
</div>
<div class="abs svc" style="left:837px;top:937px">
  <svg width="50" height="50" viewBox="0 0 50 50" fill="none" stroke="#1f3c6e" stroke-width="2"><rect x="6" y="34" width="6" height="12"/><rect x="16" y="28" width="6" height="18"/><rect x="26" y="22" width="6" height="24"/><rect x="36" y="18" width="6" height="28"/><circle cx="39" cy="8" r="6"/><path d="M39 5v6M4 46h42"/></svg>
  <h4>Marketing Strategy</h4><p>Far far away, behind the word mountains, far from the countries Vokalia.</p>
</div>
<div class="abs svc" style="left:525px;top:1202px">
  <svg width="50" height="50" viewBox="0 0 50 50" fill="none" stroke="#1f3c6e" stroke-width="2"><circle cx="22" cy="22" r="14"/><path d="M32 32l12 12M13 24l5-5 5 6 6-8"/></svg>
  <h4>Risk Analysis</h4><p>Far far away, behind the word mountains, far from the countries Vokalia.</p>
</div>
<div class="abs svc" style="left:837px;top:1202px">
  <svg width="50" height="50" viewBox="0 0 50 50" fill="none" stroke="#1f3c6e" stroke-width="2"><path d="M25 4v20M19 10l6 6 6-6M6 28l12 12h14l12-12M14 30l8 6h6"/></svg>
  <h4>Capital Market</h4><p>Far far away, behind the word mountains, far from the countries Vokalia.</p>
</div>

<!-- guidance band + stats -->
<div class="abs band" style="top:1497px;height:173px"></div>
<h2 class="abs sec-title" style="left:0;top:1538px;width:1200px;text-align:center;color:#fff;font-size:32px">You Always Get the Best Guidance</h2>
<div class="abs stats">
  <div class="stat"><div class="num">705</div><div class="lbl">PROJECTS COMPLETED</div></div>
  <div class="stat"><div class="num">809</div><div class="lbl">SATISFIED CUSTOMER</div></div>
  <div class="stat"><div class="num">335</div><div class="lbl">AWWARDS RECEIVED</div></div>
  <div class="stat"><div class="num">35</div><div class="lbl">YEARS OF EXPERIENCED</div></div>
</div>

<!-- blog -->
<h2 class="abs sec-title" style="left:0;top:1816px;width:1200px;text-align:center;font-size:32px">Recent Blog</h2>
<article class="abs post" style="left:80px;top:1938px">
  <div class="img photo" role="img" aria-label="Photo of hands over a laptop and paperwork"><div class="date"><b>30</b>April<br>2018</div></div>
  <div class="body"><h5>Northvale Loan completes structured debt investment in Brightpath</h5>
  <p>Far far away, behind the word mountains, far from the countries Vokalia and Consonantia, there live the blind texts.</p>
  <a class="btn btn-sm">Read More →</a></div>
</article>
<article class="abs post" style="left:436px;top:1938px">
  <div class="img photo" role="img" aria-label="Photo of three colleagues reviewing a document"><div class="date"><b>06</b>April<br>2016</div></div>
  <div class="body"><h5>Corvane Microsystems acquired by Lumora for $55,000,000</h5>
  <p>Far far away, behind the word mountains, far from the countries Vokalia and Consonantia, there live the blind texts.</p>
  <a class="btn btn-sm">Read More →</a></div>
</article>
<article class="abs post" style="left:792px;top:1938px">
  <div class="img photo" role="img" aria-label="Photo of two businessmen shaking hands at a desk"><div class="date"><b>19</b>OCT<br>2016</div></div>
  <div class="body"><h5>Northvale Loan completes $22,000,000 structured debt investment in Fieldnote</h5>
  <p>Far far away, behind the word mountains, far from the countries Vokalia and Consonantia, there live the blind texts.</p>
  <a class="btn btn-sm">Read More →</a></div>
</article>

<!-- clients -->
<div class="abs clients"></div>
<h2 class="abs sec-title" style="left:0;top:2602px;width:1200px;text-align:center;font-size:32px">Our Clients Says</h2>
<p class="abs" style="left:280px;top:2670px;width:640px;text-align:center;font-size:13.5px;line-height:27px">Separated they live in. A small river named Duden flows by their place and supplies it with the necessary regelialia. It is a paradisematic country</p>

<div class="abs qmark" style="left:208px;top:2812px">“</div>
<div class="abs quote" style="left:80px;top:2845px">
  <div class="avatar" role="img" aria-label="Client portrait"></div>
  <div><p>Far far away, behind the word mountains, far from the countries Vokalia and Consonantia, there live the blind texts.</p><div class="name">Mara Holt</div><div class="role">Businesswoman</div></div>
</div>
<div class="abs qmark" style="left:564px;top:2812px">“</div>
<div class="abs quote" style="left:436px;top:2845px">
  <div class="avatar" role="img" aria-label="Client portrait"></div>
  <div><p>Far far away, behind the word mountains, far from the countries Vokalia and Consonantia, there live the blind texts.</p><div class="name">Ruben Galt</div><div class="role">Businesswoman</div></div>
</div>
<div class="abs qmark" style="left:920px;top:2812px">“</div>
<div class="abs quote" style="left:792px;top:2845px">
  <div class="avatar" role="img" aria-label="Client portrait"></div>
  <div><p>Far far away, behind the word mountains, far from the countries Vokalia and Consonantia, there live the blind texts.</p><div class="name">Kenna Bosk</div><div class="role">Businesswoman</div></div>
</div>
<div class="abs c-dots"><span></span><span></span><span></span><span class="on"></span><span></span></div>

<!-- cta band -->
<div class="abs band" style="top:3180px;height:144px"></div>
<h2 class="abs sec-title" style="left:80px;top:3230px;color:#fff;font-size:32px">You Always Get the Best Guidance</h2>
<a class="abs btn" style="left:881px;top:3228px;width:239px;height:55px;background:#fff;color:var(--heading)">Connect Us</a>

<!-- footer -->
<footer class="abs footer">
  <h6 class="abs" style="left:80px;top:32px">Reach Us</h6>
  <div class="abs f-row" style="left:80px;top:82px">
    <svg width="12" height="16" viewBox="0 0 12 16"><path d="M6 0a6 6 0 0 0-6 6c0 4.5 6 10 6 10s6-5.5 6-10a6 6 0 0 0-6-6zm0 8.5A2.5 2.5 0 1 1 6 3.5a2.5 2.5 0 0 1 0 5z" fill="#fff"/></svg>
    <div>48 Alder Row, Mountain View, Sunnyvale,<br>California, USA</div>
  </div>
  <div class="abs f-row" style="left:80px;top:140px">
    <svg width="14" height="14" viewBox="0 0 24 24"><path d="M6.6 10.8a15 15 0 0 0 6.6 6.6l2.2-2.2a1 1 0 0 1 1-.2 11 11 0 0 0 3.6.6 1 1 0 0 1 1 1V20a1 1 0 0 1-1 1A17 17 0 0 1 3 4a1 1 0 0 1 1-1h3.5a1 1 0 0 1 1 1c0 1.2.2 2.5.6 3.6a1 1 0 0 1-.2 1z" fill="#fff"/></svg>
    <div>+1 555 0142 310</div>
  </div>
  <div class="abs f-row" style="left:80px;top:188px">
    <svg width="16" height="12" viewBox="0 0 16 12"><rect width="16" height="12" fill="#fff"/><path d="M0 0l8 6 8-6" stroke="#06063a" stroke-width="1.5" fill="none"/></svg>
    <div>info@northvaleloan.com</div>
  </div>

  <h6 class="abs" style="left:458px;top:32px">Links</h6>
  <div class="abs f-links" style="left:458px;top:84px">→ Home<br>→ About<br>→ Services<br>→ Projects<br>→ Contact</div>

  <h6 class="abs" style="left:614px;top:32px">Connect With Us</h6>
  <div class="abs social" style="left:615px;top:72px" aria-label="Social links"><span></span><span></span><span></span></div>

  <h6 class="abs" style="left:881px;top:32px">Subscribe Us!</h6>
  <div class="abs sub-input" style="left:881px;top:92px">Enter email address</div>
  <div class="abs sub-btn" style="left:881px;top:148px">Subscribe</div>

  <div class="abs" style="left:0;top:322px;width:1200px;text-align:center;font-size:12.5px">Copyright ©2020 NORTHVALE LOAN All rights reserved</div>
</footer>

</body>
</html>
```